Re-design of current business cards

We are updating our website with new colors and layout. Would like to re-design our business cards to co-ordinate. See attached pdf with new Brindlecraft website colors. We would also like to combine our 2 brands on the one business card. Attached is the new design for our Brindlecraft website, current business cards, which are one sided, brindlecraft logo in tiff, .ai for fonts. Brindlecraft logo font is Optimum, Quillmarsh website home page image, Quillmarsh brand statics for products which includes the logo for this brand.

Quillmarsh brand will stay the dark gray on the website. See attached statics for product and website home page.
Updates

The business cards will be 2 sided. Brindlecraft Brand on one side and Quillmarsh Brand on the other. The colors for Brindlecraft need to follow the color scheme of the brindlecraft website pdf I uploaded. The colors are a blue, lighter teal blue and white. Quillmarsh needs to follow the dark gray color on files uploaded

Target Market(s)

The trade and consumers

Industry/Entity Type

Home Furnishing

Contact Information for Business Card

We are updating our website with new colors and layout. Would like to re-design our business cards to co-ordinate. We would also like to combine our 2 brands onto 1 2 sided business cards.

Requirements
Must have
• Colors that match our new website, see attached image.
• RGB colors
• navy -#152842
• teal - 98aeb9
• The gray color used for Quillmarsh brands.
• ll logos and fonts should stay the same.

```html
<!DOCTYPE html>
<html lang="en">
<head>
<meta charset="utf-8">
<title>Brindlecraft &amp; Quillmarsh Business Cards</title>
<link rel="stylesheet" href="https://fonts.googleapis.com/css2?family=Marcellus&family=Open+Sans:wght@400;600&family=Roboto+Condensed:wght@300&display=swap">
<style>
  :root {
    --backdrop: #e4e5e6;
    --card-white: #ffffff;
    --navy: #152842;
    --teal: #98aeb9;
    --teal-deep: #8aa1ad;
    --slate: #58595b;
    --ink: #152842;
    --body-text: #2b2b2b;
    --on-dark: #eeeeee;
  }
  html, body {
    margin: 0;
    padding: 0;
    width: 1200px;
    height: 802px;
    overflow: hidden;
    background: var(--backdrop);
  }
  .sheet {
    position: relative;
    width: 1200px;
    height: 802px;
  }
  .card {
    position: absolute;
    top: 275px;
    width: 442px;
    height: 263px;
    overflow: hidden;
    box-shadow: 0 2px 6px rgba(0,0,0,0.25);
  }
  .card--front { left: 136px; background: var(--card-white); }
  .card--back  { left: 625px; background: var(--teal); }

  /* Front */
  .front-band {
    position: absolute;
    left: 0; top: 24px;
    width: 100%; height: 51px;
    background: var(--teal);
  }
  .brand-dot {
    position: absolute;
    left: 183px; top: 11px;
    width: 78px; height: 78px;
    border-radius: 50%;
    background: var(--navy);
    border: 6px solid var(--card-white);
    box-sizing: border-box;
  }
  .wordmark {
    position: absolute;
    left: 0; top: 80px;
    width: 100%;
    text-align: center;
    font-family: "Marcellus", serif;
    font-size: 40px;
    line-height: 44px;
    color: var(--ink);
    letter-spacing: 1px;
  }
  .person-name {
    position: absolute;
    left: 0; top: 139px;
    width: 100%;
    text-align: center;
    font-family: "Open Sans", sans-serif;
    font-weight: 600;
    font-size: 15px;
    color: var(--navy);
    letter-spacing: 0.5px;
  }
  .person-title {
    position: absolute;
    left: 0; top: 159px;
    width: 100%;
    text-align: center;
    font-family: "Open Sans", sans-serif;
    font-size: 12.5px;
    color: var(--body-text);
  }
  .address {
    position: absolute;
    right: 236px; top: 186px;
    text-align: right;
    font-family: "Open Sans", sans-serif;
    font-style: normal;
    font-size: 12.5px;
    line-height: 16px;
    color: var(--body-text);
  }
  .divider {
    position: absolute;
    left: 222px; top: 188px;
    width: 1px; height: 46px;
    background: var(--body-text);
  }
  .contact {
    position: absolute;
    left: 240px; top: 186px;
    font-family: "Open Sans", sans-serif;
    font-size: 12.5px;
    line-height: 16px;
    color: var(--body-text);
    list-style: none;
    margin: 0; padding: 0;
  }
  .contact li { display: flex; align-items: center; gap: 6px; }
  .contact svg { width: 10px; height: 10px; fill: var(--navy); }

  /* Back */
  .back-pattern {
    position: absolute;
    inset: 0;
    background: linear-gradient(180deg, var(--teal), var(--teal-deep));
  }
  .back-band {
    position: absolute;
    left: 0; top: 40px;
    width: 100%; height: 107px;
    background: var(--slate);
  }
  .sub-brand {
    position: absolute;
    left: 0; top: 16px;
    width: 100%;
    text-align: center;
    font-family: "Marcellus", serif;
    font-size: 29px;
    line-height: 32px;
    color: var(--card-white);
    letter-spacing: 0.5px;
  }
  .sub-brand-by {
    position: absolute;
    right: 127px; top: 47px;
    font-family: "Marcellus", serif;
    font-size: 6px;
    color: var(--card-white);
    letter-spacing: 0.3px;
  }
  .tagline {
    position: absolute;
    left: 0; top: 75px;
    width: 100%;
    text-align: center;
    font-family: "Roboto Condensed", sans-serif;
    font-weight: 300;
    font-size: 13.5px;
    color: var(--on-dark);
  }
</style>
</head>
<body>
<main class="sheet">
  <section class="card card--front" aria-label="Brindlecraft business card front">
    <div class="front-band"></div>
    <div class="brand-dot" aria-hidden="true"></div>
    <div class="wordmark">BRINDLECRAFT</div>
    <div class="person-name">MARION LANFORD</div>
    <div class="person-title">Graphics/Photography Director</div>
    <address class="address">
      PO Box 412/1870<br>
      Alder Bend Rd<br>
      Fairlee, Vermont 05045
    </address>
    <div class="divider"></div>
    <ul class="contact">
      <li>
        <svg viewBox="0 0 10 10" aria-hidden="true"><path d="M1 3.5C1 2 2.2 1.5 5 1.5S9 2 9 3.5L7.5 4.2 6.8 3H3.2L2.5 4.2Z M2.3 5h5.4l.8 3.5H1.5Z"/></svg>
        555.201.4837
      </li>
      <li>
        <svg viewBox="0 0 10 10" aria-hidden="true"><path d="M2.5 1h5v2.5h-5Z M1 4h8v3.5H7.5V6h-5v1.5H1Z M3 6.8h4V9H3Z"/></svg>
        555.201.4862
      </li>
      <li>
        <svg viewBox="0 0 10 10" aria-hidden="true"><path d="M1 2.5h8v5H1Z"/><path d="M1 2.5 5 5.5 9 2.5" fill="none" stroke="#fff" stroke-width="0.8"/></svg>
        mlanford@brindlecraft.com
      </li>
    </ul>
  </section>

  <section class="card card--back" aria-label="Quillmarsh business card back">
    <div class="back-pattern" role="img" aria-label="Faint repeating pattern of the brand symbol in soft teal tones"></div>
    <div class="back-band">
      <div class="sub-brand">QUILLMARSH</div>
      <div class="sub-brand-by">by BRINDLECRAFT</div>
      <div class="tagline">Discover the luxury of home.</div>
    </div>
  </section>
</main>
</body>
</html>
```